Moden - Mexicali - Flower Shop

brisapetals is looking for a cool web design that has a airy, clean, mexicali feel to it.

See attached images and links for idea of what we mean with the above.

please no templates.

Target Market(s)

Local flower shop in San Diego, California

Industry/Entity Type

Shop

Requirements
Must have
• see. brisapetals.quartzcart.example - I did the site and logo...I love the logo - hate the site.

Going for this feel: http://www.velmorastudio.example/platebook/archives/tovarinos.php

I also attached another site I liked- I just feel like it may be to busy.

```html
<!DOCTYPE html>
<html lang="en">
<head>
<meta charset="utf-8">
<title>Brisapetals — Fresh Flowers of San Diego</title>
<link href="https://fonts.googleapis.com/css2?family=Alegreya:wght@400;700;800;900&family=Open+Sans:wght@400;600&family=Yellowtail&display=swap" rel="stylesheet">
<style>
:root{
  --teal:#6aab95;
  --teal-dark:#4f9a86;
  --white:#ffffff;
  --ink:#2a2a2a;
  --price:#d9343a;
  --strike:#6aab95;
  --yellow:#f4df45;
  --paper-light:#efd7a2;
  --paper:#e3c07e;
  --paper-dark:#c99e56;
  --footer:#323232;
  --footer-text:#e8e8e8;
}
*{box-sizing:border-box;margin:0;padding:0}
html,body{width:846px;height:1200px;overflow:hidden;background:var(--white)}
body{font-family:"Open Sans",sans-serif;color:var(--ink);position:relative}
.abs{position:absolute}

/* top bar */
.topbar{left:0;top:0;width:846px;height:30px;background:var(--teal);color:var(--white);font-size:10px}
.topbar .account{left:77px;top:8px}
.topbar .cart{left:215px;top:8px;display:flex;align-items:center;gap:6px}
.search{left:652px;top:8px;width:118px;height:15px;background:var(--white);border-radius:8px;font-size:8px;color:#9a9a9a;padding:2px 8px}
.search svg{position:absolute;right:7px;top:3px}

/* header */
.header{left:0;top:30px;width:846px;height:56px;background:var(--white);box-shadow:0 1px 3px rgba(0,0,0,.15);z-index:2}
.brand{left:77px;top:14px;display:flex;align-items:center;gap:10px;font-family:"Alegreya",serif;font-size:26px;letter-spacing:6px;color:var(--teal)}
.brand .mark{width:26px;height:26px;border-radius:50%;border:2px solid var(--teal)}
.nav{left:486px;top:22px;display:flex;gap:28px;font-family:"Alegreya",serif;font-weight:800;font-size:13px;letter-spacing:1.2px}
.nav a{color:var(--ink);text-decoration:none}
.nav a.current{color:var(--teal)}

/* hero */
.hero{left:0;top:86px;width:846px;height:387px;background:
  radial-gradient(ellipse at 80% 60%,#b0207f 0%,#7d1763 35%,transparent 65%),
  radial-gradient(ellipse at 20% 40%,#c03a95 0%,#6a2a5a 40%,transparent 70%),
  linear-gradient(90deg,#9aa08e 0%,#5b3a55 20%,#3c2a3a 50%,#8e2a78 100%)}
.hero-title{left:0;width:846px;text-align:center;color:var(--white);font-family:"Alegreya",serif;font-weight:900;text-shadow:4px 4px 0 #5b1b5d}
.hero-title.big{top:150px;font-size:100px;letter-spacing:14px;line-height:1}
.hero-title.mid{top:252px;font-size:62px;letter-spacing:11px;line-height:1}
.hero-script{left:0;width:846px;top:315px;text-align:center;font-family:"Yellowtail",cursive;font-size:44px;color:var(--white);line-height:1}
.btn-shop{left:349px;top:382px;width:147px;height:37px;background:var(--yellow);border-bottom:3px solid var(--teal-dark);text-align:center;font-family:"Alegreya",serif;font-weight:800;font-size:17px;letter-spacing:1px;color:var(--teal-dark);line-height:35px}
.dots{left:403px;top:437px;display:flex;gap:6px}
.dots span{width:10px;height:10px;border-radius:50%;background:var(--white)}
.dots span.on{background:var(--yellow)}

/* paper section */
.paper{left:0;top:473px;width:846px;height:575px;background:
  radial-gradient(ellipse at 50% 40%,var(--paper-light) 0%,var(--paper) 60%,var(--paper-dark) 100%)}
.section-title{left:0;width:846px;text-align:center;font-family:"Alegreya",serif;font-weight:800;font-size:50px;color:var(--ink);line-height:1}
.rule{height:8px;border-top:2px solid var(--teal);border-bottom:2px solid var(--teal)}
.arrow{width:20px;height:30px}

.card{background:var(--white);box-shadow:0 1px 3px rgba(0,0,0,.2)}
.card .photo{position:absolute;left:0;right:0}
.product .name{position:absolute;left:6px;top:133px;font-family:"Alegreya",serif;font-size:16px;color:var(--teal)}
.product .price{position:absolute;right:8px;top:135px;font-family:"Alegreya",serif;font-size:14px;color:var(--price)}
.product .price s{color:var(--strike)}
.card-base{height:14px;background:repeating-linear-gradient(135deg,rgba(0,0,0,.07) 0 2px,transparent 2px 5px)}
.buy{width:66px;height:19px}
.buy span{position:absolute;left:0;top:0;width:60px;text-align:center;font-family:"Alegreya",serif;font-weight:800;font-size:11px;line-height:19px;color:var(--ink)}

.collection .title{position:absolute;left:0;right:0;top:118px;text-align:center;font-family:"Alegreya",serif;font-size:16px;color:var(--teal)}
.collection .count{position:absolute;left:0;right:0;top:137px;text-align:center;font-family:"Alegreya",serif;font-size:11px;color:var(--ink)}

/* footer */
.footer{left:0;top:1048px;width:846px;height:130px;background:var(--footer);color:var(--footer-text);font-size:9.5px;line-height:15px}
.footer h3{font-family:"Alegreya",serif;font-weight:800;font-size:19px;color:var(--teal);margin-bottom:10px;line-height:1}
.footer .col{position:absolute;top:14px}
.signup{display:flex;margin-top:8px}
.signup .field{width:95px;height:21px;background:var(--white);color:#aaa;font-size:8px;padding:3px 6px}
.signup .go{width:42px;height:21px;background:var(--yellow);color:var(--ink);font-size:8px;font-weight:600;text-align:center;line-height:21px}
.social{display:flex;gap:3px}
.social span{width:14px;height:14px;border-radius:50%;background:var(--yellow)}

.bottombar{left:0;top:1178px;width:846px;height:22px;background:var(--white);font-size:9px;color:var(--ink)}
.bottombar .copy{left:77px;top:5px}
.bottombar .links{right:76px;top:5px;display:flex;gap:20px}
</style>
</head>
<body>

<div class="abs topbar">
  <div class="abs account">Log in or Create an account</div>
  <div class="abs cart">
    <svg width="13" height="11" viewBox="0 0 13 11"><path d="M0 1h2.5l1.8 6h6.5l1.5-4.5H3.5" fill="none" stroke="#fff" stroke-width="1.4"/><circle cx="5" cy="9.5" r="1.2" fill="#fff"/><circle cx="10" cy="9.5" r="1.2" fill="#fff"/></svg>
    0 items · Check out
  </div>
  <div class="abs search">Search store....
    <svg width="9" height="9" viewBox="0 0 9 9"><circle cx="3.7" cy="3.7" r="2.8" fill="none" stroke="#6aab95" stroke-width="1.3"/><path d="M5.8 5.8L8.5 8.5" stroke="#6aab95" stroke-width="1.4"/></svg>
  </div>
</div>

<div class="abs header">
  <div class="abs brand"><span class="mark"></span>BRISAPETALS</div>
  <nav class="abs nav">
    <a class="current">HOME</a><a>SHOP</a><a>CURATED</a><a>ABOUT US</a>
  </nav>
</div>

<section class="abs hero" role="img" aria-label="Close-up photo of purple and magenta petunias in bloom">
</section>
<div class="abs hero-title big">PURPLE</div>
<div class="abs hero-title mid">SUMMER</div>
<div class="abs hero-script">bouquet</div>
<div class="abs btn-shop">SHOP NOW</div>
<div class="abs dots"><span class="on"></span><span></span><span></span></div>

<section class="abs paper" aria-label="Featured products">
</section>

<!-- Fresh This Week -->
<div class="abs rule" style="left:77px;top:519px;width:155px"></div>
<div class="abs rule" style="left:612px;top:519px;width:157px"></div>
<h2 class="abs section-title" style="top:495px">Fresh This Week</h2>

<svg class="abs arrow" style="left:43px;top:620px" viewBox="0 0 20 30"><path d="M15 3L4 15l11 12" fill="none" stroke="#fff" stroke-width="4.5"/></svg>
<svg class="abs arrow" style="left:783px;top:620px" viewBox="0 0 20 30"><path d="M5 3l11 12L5 27" fill="none" stroke="#fff" stroke-width="4.5"/></svg>

<div class="abs card product" style="left:77px;top:556px;width:219px;height:177px">
  <div class="photo" role="img" aria-label="Photo of orange tiger lilies" style="top:10px;height:110px;background:linear-gradient(135deg,#f39a2a,#e8761b 50%,#8a6a3a)"></div>
  <div class="name">California Lillies</div>
  <div class="price">$ 50.00 <s>$ 75.00</s></div>
</div>
<div class="abs card product" style="left:313px;top:556px;width:218px;height:177px">
  <div class="photo" role="img" aria-label="Photo of red roses with green leaves" style="top:10px;height:110px;background:linear-gradient(135deg,#b5121b,#d7262c 45%,#3f6b2a)"></div>
  <div class="name">Ruby Roses</div>
  <div class="price">$ 40.00 <s>$ 75.00</s></div>
</div>
<div class="abs card product" style="left:551px;top:556px;width:219px;height:177px">
  <div class="photo" role="img" aria-label="Photo of red and yellow spring tulips" style="top:10px;height:110px;background:linear-gradient(180deg,#b9d98a,#e7452b 55%,#5c9a3a)"></div>
  <div class="name">Spring time</div>
  <div class="price">$ 50.00 <s>$ 60.00</s></div>
</div>
<div class="abs card-base" style="left:77px;top:733px;width:219px"></div>
<div class="abs card-base" style="left:313px;top:733px;width:218px"></div>
<div class="abs card-base" style="left:551px;top:733px;width:219px"></div>

<div class="abs buy" style="left:154px;top:723px"><svg width="66" height="19" viewBox="0 0 66 19"><path d="M0 0h58l8 9.5-8 9.5H0z" fill="#f4df45"/></svg><span>BUY</span></div>
<div class="abs buy" style="left:390px;top:723px"><svg width="66" height="19" viewBox="0 0 66 19"><path d="M0 0h58l8 9.5-8 9.5H0z" fill="#f4df45"/></svg><span>BUY</span></div>
<div class="abs buy" style="left:627px;top:723px"><svg width="66" height="19" viewBox="0 0 66 19"><path d="M0 0h58l8 9.5-8 9.5H0z" fill="#f4df45"/></svg><span>BUY</span></div>

<!-- Curated Collections -->
<div class="abs rule" style="left:77px;top:791px;width:112px"></div>
<div class="abs rule" style="left:655px;top:791px;width:114px"></div>
<h2 class="abs section-title" style="top:767px">Curated Collections</h2>

<svg class="abs arrow" style="left:43px;top:898px" viewBox="0 0 20 30"><path d="M15 3L4 15l11 12" fill="none" stroke="#fff" stroke-width="4.5"/></svg>
<svg class="abs arrow" style="left:783px;top:898px" viewBox="0 0 20 30"><path d="M5 3l11 12L5 27" fill="none" stroke="#fff" stroke-width="4.5"/></svg>

<div class="abs card collection" style="left:77px;top:828px;width:170px;height:174px">
  <div class="photo" role="img" aria-label="Photo of pink and white stargazer lilies" style="top:10px;height:110px;background:linear-gradient(135deg,#4f7a3a,#e6a7c4 50%,#5b8a3e)"></div>
  <div class="title">Any Occasion</div><div class="count">2 products</div>
</div>
<div class="abs card collection" style="left:252px;top:828px;width:168px;height:174px">
  <div class="photo" role="img" aria-label="Photo of pink gerbera daisies wrapped in kraft paper" style="top:10px;height:110px;background:linear-gradient(135deg,#8a8a80,#e8457a 45%,#c49a6a)"></div>
  <div class="title">Birthday</div><div class="count">1 products</div>
</div>
<div class="abs card collection" style="left:427px;top:828px;width:169px;height:174px">
  <div class="photo" role="img" aria-label="Photo of white calla lilies on grey wood" style="top:10px;height:110px;background:linear-gradient(135deg,#6e6a64,#e9e9e2 50%,#4d6a3a)"></div>
  <div class="title">Dude</div><div class="count">1 products</div>
</div>
<div class="abs card collection" style="left:601px;top:828px;width:169px;height:174px">
  <div class="photo" role="img" aria-label="Photo of a mass of deep red roses" style="top:10px;height:110px;background:linear-gradient(135deg,#7c0f1c,#b11e2c 50%,#6a0d18)"></div>
  <div class="title">Love</div><div class="count">1 products</div>
</div>
<div class="abs card-base" style="left:77px;top:1002px;width:170px"></div>
<div class="abs card-base" style="left:252px;top:1002px;width:168px"></div>
<div class="abs card-base" style="left:427px;top:1002px;width:169px"></div>
<div class="abs card-base" style="left:601px;top:1002px;width:169px"></div>

<footer class="abs footer">
  <div class="col" style="left:77px;width:185px">
    <h3>Meet Brisa</h3>
    <p>Based in Hillcrest, San Diego - We offer farm fresh, curated, cool, and same day delivery flower bouquets.</p>
  </div>
  <div class="col" style="left:295px;width:160px">
    <h3>Reach Brisa</h3>
    <p>2210 Alder Street<br>San Diego, CA 92104</p>
    <p style="margin-top:13px">Email: info@brisapetals.com<br>Phone: 619-555-0148</p>
  </div>
  <div class="col" style="left:474px;width:190px">
    <h3>Newsletter</h3>
    <p>We promise to only send you good things like discounts!</p>
    <div class="signup"><div class="field">Your email..</div><div class="go">SIGN UP</div></div>
  </div>
  <div class="col" style="left:680px;width:100px">
    <h3>Follow Us</h3>
    <div class="social"><span></span><span></span><span></span></div>
  </div>
</footer>

<div class="abs bottombar">
  <div class="abs copy">Copyright © 2014 brisapetals of San Diego.</div>
  <div class="abs links"><span>Home</span><span>Shop</span><span>Curated</span><span>About Us</span></div>
</div>

</body>
</html>
```